Garage Door Sales and Repair Website

Looking for a website theme and home page design for a garage door sales and repair company (Copper Ridge Garage).   We have a new logo and color scheme (attached) and need to update our website to match.  Here is the current site http://www.copperridgegarage.example/
The design should lend it self to being responsive and full screen.
I like this site (http://www.bluefern-site-works.example/) how it has different color blocks and I would like to have a slide show on my home page as well.  4 slides utilizing some of the following concepts Garage Opener, Garage Doors, Springs, Garage Door Repair, Specials, Free Estimate, etc...
Would like color design to match logo / business cards attached.
Call for Free Estimate with phone number should be visible on top of the page as well.

Target Market(s)
Consumers
Industry/Entity Type
Professional Service
Number of Pages Required
1 page
Font styles to use
Other font styles liked:
- Oswald, Open Sans, other similar google web fonts

Requirements
Must have
- 4 slides for home page design
- Free Estimate
- Phone Number

Nice to have
- Call out for online specials

```html
<!DOCTYPE html>
<html lang="en">
<head>
<meta charset="utf-8">
<title>Copper Ridge Garage – Garage Door Sales and Repair</title>
<link href="https://fonts.googleapis.com/css2?family=Raleway:wght@500;600;700;800&family=Open+Sans:wght@400;600;700&display=swap" rel="stylesheet">
<style>
:root{
  --navy:#3e4a7a;
  --navy-dark:#333f6b;
  --orange:#f57a0d;
  --ink:#3b3f55;
  --muted:#5d6378;
  --pale:#e3e8f0;
  --band:#b8c5d5;
  --card:#eef1f6;
  --white:#ffffff;
  --bar:#cbd3df;
}
*{box-sizing:border-box;margin:0;padding:0}
html,body{width:1200px;height:3689px;overflow:hidden}
body{font-family:"Open Sans",Arial,sans-serif;color:var(--ink);background:var(--white);position:relative}
.section{position:absolute;left:0;width:1200px}
.abs{position:absolute}
.btn{position:absolute;display:flex;align-items:center;justify-content:center;font-family:"Raleway",Arial,sans-serif;font-weight:700;text-transform:uppercase;text-decoration:none;font-size:16px;letter-spacing:.3px}
.btn-orange{background:var(--orange);color:var(--white)}
.btn-outline{border:2px solid var(--ink);color:var(--ink);background:var(--white)}

/* hero */
.hero{top:0;height:602px;overflow:hidden}
.hero-photo{position:absolute;inset:0;background:linear-gradient(180deg,#6f89b8 0%,#a9bfdc 25%,#8c8a86 45%,#6a6e6c 62%,#5e8a3e 82%,#4f7a33 100%)}
.hero-shade{position:absolute;left:0;top:0;width:1200px;height:150px;background:linear-gradient(180deg,rgba(30,38,70,.75),rgba(30,38,70,0))}
.brand{position:absolute;left:74px;top:22px;display:flex;align-items:center;gap:14px}
.brand-mark{width:30px;height:30px;border-radius:50%;background:var(--white)}
.brand-name{font-family:"Raleway",Arial,sans-serif;font-weight:800;font-size:26px;color:var(--white);text-transform:uppercase;line-height:1}
.call{position:absolute;right:74px;top:22px;font-family:"Raleway",Arial,sans-serif;font-weight:600;font-size:27px;color:var(--white);text-transform:uppercase}
.call strong{font-weight:800}
.nav{position:absolute;right:74px;top:78px;display:flex;gap:4px}
.nav a{font-family:"Raleway",Arial,sans-serif;font-weight:700;font-size:14px;color:var(--white);text-decoration:none;text-transform:uppercase;padding:9px 12px}
.nav a.active{border:2px solid var(--white);padding:7px 12px}
.hero-title{position:absolute;left:74px;top:310px;font-family:"Raleway",Arial,sans-serif;font-weight:800;font-size:39px;line-height:46px;color:var(--white);text-transform:uppercase;text-shadow:0 2px 6px rgba(0,0,0,.35)}
.hero .btn{left:74px;top:470px;width:273px;height:54px}
.dots{position:absolute;left:568px;top:555px;display:flex;gap:8px}
.dots span{width:10px;height:10px;border-radius:50%;background:var(--white);opacity:.7}
.dots span:first-child{opacity:1}
.hero-wave{position:absolute;left:0;bottom:0}

/* section headings */
.section-head{position:absolute;left:0;width:1200px;text-align:center}
.section-mark{width:92px;height:92px;border-radius:50%;border:3px solid var(--navy);margin:0 auto;background:var(--white)}
.section-head h2{font-family:"Raleway",Arial,sans-serif;font-weight:800;font-size:32px;color:var(--navy);text-transform:uppercase;margin-top:-34px;background:inherit;display:inline-block;padding:0 10px;position:relative}
.services .section-head h2{background:var(--white)}
.about .section-head h2{background:var(--pale)}
.specials .section-head h2{background:var(--white)}

/* services */
.services{top:602px;height:733px}
.service-card{position:absolute;top:165px;width:332px;height:413px;background:var(--card);box-shadow:0 4px 6px rgba(0,0,0,.08)}
.service-photo{height:212px}
.service-card h3{font-family:"Raleway",Arial,sans-serif;font-weight:700;font-size:17px;color:var(--navy);text-transform:uppercase;text-align:center;margin-top:27px}
.service-card p{font-size:14px;line-height:26px;color:var(--muted);text-align:center;padding:8px 22px 0}

/* about */
.about{top:1335px;height:731px;background:var(--pale)}
.about-intro{position:absolute;left:74px;top:166px;width:1052px;text-align:center;font-size:14px;line-height:26px;color:var(--muted)}
.about-photo{position:absolute;left:74px;top:244px;width:514px;height:420px;background:linear-gradient(135deg,#d8d3c8 0%,#a9a49a 40%,#2f5aa8 65%,#1f3f86 100%)}
.feature{position:absolute;left:612px;display:flex;gap:28px}
.feature-icon{width:60px;height:60px;border-radius:50%;border:2px solid var(--navy);background:var(--white);display:flex;align-items:center;justify-content:center;flex:none}
.feature h4{font-family:"Raleway",Arial,sans-serif;font-weight:700;font-size:16px;color:var(--navy);text-transform:uppercase;margin-top:0}
.feature p{font-size:14px;line-height:24px;color:var(--muted);margin-top:4px}
.promise{top:2066px;height:241px;background:var(--band)}
.promise-notch{position:absolute;left:645px;top:-1px}
.promise p{position:absolute;left:100px;top:46px;width:1000px;text-align:center;font-size:14px;line-height:26px;color:var(--ink)}
.promise .btn{left:465px;top:145px;width:268px;height:54px}

/* specials */
.specials{top:2307px;height:914px}
.specials-lead{position:absolute;top:162px;width:1200px;text-align:center;font-family:"Raleway",Arial,sans-serif;font-weight:700;font-size:23px;color:var(--ink);text-transform:uppercase}
.specials-tag{position:absolute;top:203px;width:1200px;text-align:center;font-family:"Raleway",Arial,sans-serif;font-weight:700;font-size:17px;color:var(--navy)}
.special{position:absolute;top:349px;width:244px;height:260px;background:var(--pale);text-align:center}
.special-badge{position:absolute;left:57px;top:-86px;width:130px;height:130px;border-radius:50%;background:var(--navy);border:5px solid var(--white);box-shadow:0 0 0 2px var(--navy);display:flex;flex-direction:column;align-items:center;justify-content:center;color:var(--white);font-family:"Raleway",Arial,sans-serif;font-weight:800;line-height:1}
.special-badge .amount{font-size:36px}
.special-badge .off{font-size:30px;margin-top:2px}
.special-badge .small{font-size:15px;margin-top:6px}
.special h3{margin-top:60px;font-family:"Raleway",Arial,sans-serif;font-weight:800;font-size:21px;line-height:24px;color:var(--ink);text-transform:uppercase;padding:0 16px}
.special p{font-size:13px;line-height:20px;color:var(--ink);margin-top:10px;padding:0 26px}
.special .btn{left:20px;top:189px;width:204px;height:45px;font-size:13px;font-family:"Open Sans",Arial,sans-serif}
.specials-note{position:absolute;top:652px;width:1200px;text-align:center;font-size:13px;color:var(--muted)}
.specials-rule{position:absolute;left:74px;top:697px;width:1052px;height:1px;background:#d7dce5}
.badge-plain{position:absolute}

/* footer */
.footer{top:3221px;height:369px}
.footer-bg{position:absolute;left:0;top:0}
.footer-col{position:absolute;top:123px}
.footer-col h5{font-family:"Raleway",Arial,sans-serif;font-weight:700;font-size:16px;line-height:22px;color:var(--white);text-transform:uppercase;margin-bottom:10px}
.footer-col li{list-style:none;font-size:13px;line-height:28px;color:#dfe4ef}
.footer-col li.more{font-weight:700;color:var(--white)}
.contact-line{display:flex;align-items:center;gap:10px}
.bottom-bar{top:3590px;height:99px;background:var(--bar)}
.copyright{position:absolute;left:76px;top:40px;font-size:13px;color:var(--muted)}
.social{position:absolute;right:74px;top:32px;display:flex;gap:8px}
.social span{width:32px;height:32px;border-radius:50%;background:var(--navy)}
</style>
</head>
<body>

<header class="section hero">
  <div class="hero-photo" role="img" aria-label="Photo of a suburban house with a wide grey garage door and green lawn"></div>
  <div class="hero-shade"></div>
  <div class="brand"><span class="brand-mark"></span><span class="brand-name">Copper Ridge Garage</span></div>
  <div class="call">Call for free estimate: <strong>303-555-0147</strong></div>
  <nav class="nav">
    <a class="active" href="#">Home</a><a href="#">Openers</a><a href="#">Garage Doors</a><a href="#">Broken Springs</a><a href="#">Garage Door Repair</a><a href="#">Blog</a>
  </nav>
  <h1 class="hero-title">Denver’s preferred<br>garage door sales and<br>repair company</h1>
  <a class="btn btn-orange" href="#">Schedule free estimate</a>
  <div class="dots"><span></span><span></span><span></span><span></span></div>
  <svg class="hero-wave" width="1200" height="70" viewBox="0 0 1200 70">
    <path d="M0 36 Q600 -6 1200 36 L1200 70 L0 70 Z" fill="#ffffff"/>
    <path d="M0 36 Q600 -6 1200 36" fill="none" stroke="#3e4a7a" stroke-width="4"/>
  </svg>
</header>

<section class="section services">
  <div class="section-head" style="top:33px"><div class="section-mark"></div><h2>Our Services</h2></div>
  <article class="service-card" style="left:74px">
    <div class="service-photo" role="img" aria-label="Photo of a technician repairing a garage door" style="background:linear-gradient(135deg,#e8e8e8 0%,#c9cfd8 45%,#2f4fa0 75%,#23407f 100%)"></div>
    <h3>Garage Door Repair</h3>
    <p>Copper Ridge Garage offers complete garage door repair and door maintenance services. Damaged panels, bent tracks, damaged rollers, broken springs, worn weather seal and doors...</p>
  </article>
  <article class="service-card" style="left:435px">
    <div class="service-photo" role="img" aria-label="Photo of a ceiling-mounted garage door opener" style="background:linear-gradient(180deg,#e9ecef 0%,#cfd4da 55%,#8d939b 100%)"></div>
    <h3>Garage Door Openers</h3>
    <p>Copper Ridge Garage offers complete garage door repair and door maintenance services. Damaged panels, bent tracks, damaged rollers, broken springs, worn weather seal and doors...</p>
  </article>
  <article class="service-card" style="left:794px">
    <div class="service-photo" role="img" aria-label="Photo of two white carriage-style garage doors on a navy wall" style="background:linear-gradient(180deg,#2c3f78 0%,#2c3f78 18%,#f1f2f4 22%,#dfe2e6 100%)"></div>
    <h3>New Garage Doors</h3>
    <p>Copper Ridge Garage offers complete garage door repair and door maintenance services. Damaged panels, bent tracks, damaged rollers, broken springs, worn weather seal and doors...</p>
  </article>
  <a class="btn btn-orange" href="#" style="left:320px;top:628px;width:270px;height:54px">Schedule free estimate</a>
  <a class="btn btn-outline" href="#" style="left:607px;top:628px;width:271px;height:54px">View all services</a>
</section>

<section class="section about">
  <div class="section-head" style="top:27px"><div class="section-mark"></div><h2>About Us</h2></div>
  <p class="about-intro">Copper Ridge Garage Door Sales and Repair (Copper Ridge Garage) is a locally owned and operated garage door company that specializes in everything from garage door repairs to installation of new garage doors to garage door service and installation of garage door openers.</p>
  <div class="about-photo" role="img" aria-label="Photo of a technician in a blue shirt fitting garage door hardware"></div>

  <div class="feature" style="top:246px">
    <div class="feature-icon"><svg width="30" height="30" viewBox="0 0 30 30"><text x="15" y="23" text-anchor="middle" font-family="Open Sans, sans-serif" font-size="24" font-weight="700" fill="#3e4a7a">$</text></svg></div>
    <div><h4>Honesty</h4><p>Our reputation is important to us and so is your satisfaction.<br>No hidden costs or un-needed add-ons!</p></div>
  </div>
  <div class="feature" style="top:342px">
    <div class="feature-icon"><svg width="28" height="28" viewBox="0 0 28 28"><circle cx="14" cy="9" r="6" fill="#3e4a7a"/><path d="M3 27 Q3 16 14 16 Q25 16 25 27 Z" fill="#3e4a7a"/></svg></div>
    <div><h4>Dependability</h4><p>Fast, friendly reliable service from qualified technicians.</p></div>
  </div>
  <div class="feature" style="top:426px">
    <div class="feature-icon"><svg width="28" height="28" viewBox="0 0 28 28"><path d="M4 15 L11 22 L24 7" fill="none" stroke="#3e4a7a" stroke-width="4" stroke-linecap="round" stroke-linejoin="round"/></svg></div>
    <div><h4>Satisfaction Guaranteed.</h4><p>We guarantee all our work</p></div>
  </div>
  <div class="feature" style="top:509px">
    <div class="feature-icon"><svg width="26" height="30" viewBox="0 0 26 30"><path d="M3 2 H17 L23 8 V28 H3 Z" fill="#3e4a7a"/><path d="M7 14 H19 M7 19 H19 M7 24 H15" stroke="#fff" stroke-width="2"/></svg></div>
    <div><h4>Free Estimates</h4><p>Don't get blindsided by unexpected sur-charges etc.<br>get a free quote today.</p></div>
  </div>
  <div class="feature" style="top:603px">
    <div class="feature-icon"><svg width="28" height="28" viewBox="0 0 28 28"><path d="M7 3 L11 8 L8.5 11 Q11 17 17 19.5 L20 17 L25 21 L22 25 Q12 25 5 17 Q2 11 3 6 Z" fill="#3e4a7a"/></svg></div>
    <div><h4>24 Emergency Service</h4><p>Our Technicians are available 24 hours a day 7 days a week.<br>No extra charge for weekends.</p></div>
  </div>
</section>

<section class="section promise">
  <svg class="promise-notch" width="40" height="22" viewBox="0 0 40 22"><path d="M0 0 H40 L20 20 Z" fill="#e3e8f0"/></svg>
  <p>We are dedicated to the highest quality professional service and complete customer satisfaction. We take pride in serving our customers and providing the best possible service experience on each appointment we schedule, and we maintain our reputation by being honest and dependable.</p>
  <a class="btn btn-orange" href="#">Schedule free estimate</a>
</section>

<section class="section specials">
  <div class="section-head" style="top:28px"><div class="section-mark"></div><h2>Specials</h2></div>
  <p class="specials-lead">Same day garage door repair &amp; service</p>
  <p class="specials-tag">Fast – Affordable – Professional – No Additional Charge For Weekends – 24 Hour Emergency Service Available</p>

  <article class="special" style="left:76px">
    <div class="special-badge"><span class="amount">$60</span><span class="off">OFF</span></div>
    <h3>Spring<br>Replacement</h3>
    <p>$60 off Replacement of Two Garage Door Springs</p>
    <a class="btn btn-orange" href="#">Schedule free estimate</a>
  </article>
  <article class="special" style="left:344px">
    <div class="special-badge"><span class="amount">$100</span><span class="off">OFF</span></div>
    <h3>New Garage<br>Door</h3>
    <p>Purchase and Installation of any Single Door</p>
    <a class="btn btn-orange" href="#">Schedule free estimate</a>
  </article>
  <article class="special" style="left:612px">
    <div class="special-badge"><span class="amount">$200</span><span class="off">OFF</span></div>
    <h3>New Garage<br>Door</h3>
    <p>$200 off Purchase and Installation of any Double Door</p>
    <a class="btn btn-orange" href="#">Schedule free estimate</a>
  </article>
  <article class="special" style="left:883px">
    <div class="special-badge"><span class="amount">$325</span><span class="small">OVERHAUL</span></div>
    <h3>Best Value</h3>
    <p>Overhaul includes new Springs, Rollers, Cables, Pulleys &amp; Bearings</p>
    <a class="btn btn-orange" href="#">Schedule free estimate</a>
  </article>

  <p class="specials-note">*** Must present / mention coupon at time of estimate. Not valid with other offers</p>
  <div class="specials-rule"></div>

  <svg class="badge-plain" style="left:325px;top:779px" width="201" height="86" viewBox="0 0 201 86"><rect width="201" height="86" rx="6" fill="#1e1e1e"/></svg>
  <svg class="badge-plain" style="left:585px;top:768px" width="148" height="108" viewBox="0 0 148 108"><circle cx="74" cy="52" r="50" fill="#b5a57a"/></svg>
  <svg class="badge-plain" style="left:795px;top:782px" width="83" height="83" viewBox="0 0 83 83"><circle cx="41.5" cy="41.5" r="40" fill="#2f6fb0"/></svg>
</section>

<footer class="section footer">
  <svg class="footer-bg" width="1200" height="369" viewBox="0 0 1200 369">
    <path d="M0 60 Q600 -10 1200 50 L1200 369 L0 369 Z" fill="#3e4a7a"/>
    <path d="M0 48 Q600 -22 1200 38" fill="none" stroke="#3e4a7a" stroke-width="5"/>
    <path d="M0 60 Q600 -10 1200 50" fill="none" stroke="#ffffff" stroke-width="5"/>
  </svg>
  <div class="footer-col" style="left:76px">
    <h5>Quick Links</h5>
    <ul><li>Home</li><li>About Us</li><li>Services</li><li>Latest News</li><li>Blog</li><li>Contact Us</li></ul>
  </div>
  <div class="footer-col" style="left:278px">
    <h5>Garage Door Products<br>&amp; Services</h5>
    <ul><li>Garage Door Repair</li><li>New Garage Doors</li><li>Garage Door Openers</li><li>Garage Door Maintenance</li><li>Garage Door Tune and Lube</li><li class="more">View All</li></ul>
  </div>
  <div class="footer-col" style="left:590px">
    <h5>Proudly Serving Denver<br>Metro Area</h5>
    <ul><li>Arvada, CO</li><li>Aurora, CO</li><li>Berkley, CO</li><li>Boulder, CO</li><li>Brighton, CO</li><li class="more">View All</li></ul>
  </div>
  <div class="footer-col" style="left:883px">
    <h5>Contact Us</h5>
    <ul>
      <li>Arvada, CO</li>
      <li style="line-height:22px;padding:3px 0">Copper Ridge Garage, 4410 Alder Crest Ave<br>Denver, CO 80021</li>
      <li class="contact-line"><svg width="12" height="12" viewBox="0 0 28 28"><path d="M7 3 L11 8 L8.5 11 Q11 17 17 19.5 L20 17 L25 21 L22 25 Q12 25 5 17 Q2 11 3 6 Z" fill="#ffffff"/></svg><strong>303-555-0147</strong></li>
      <li class="contact-line"><svg width="13" height="10" viewBox="0 0 13 10"><rect width="13" height="10" fill="#ffffff"/><path d="M0 0 L6.5 6 L13 0" fill="none" stroke="#3e4a7a" stroke-width="1.4"/></svg><strong>info@copperridgegarage.example</strong></li>
    </ul>
  </div>
</footer>

<div class="section bottom-bar">
  <p class="copyright">Copyright © 2008 - 2016 Copper Ridge Garage Sales &amp; Repair, LLC. All rights reserved.</p>
  <div class="social"><span></span><span></span><span></span><span></span><span></span><span></span></div>
</div>

</body>
</html>
```